Lady Winnow's Cask Aged Heronfield Rum LABEL

Tallowbrook Distillery is looking for a label for our new product (Lady Winnow's Cask). This will be a barrel aged Rum that is distilled, bottled, and aged in small batches in Belmont, NC just outside of Charlotte, North Carolina. In the attached file (drink recipes) you will see the Product that we currently sell (Heronfield Rum). The new product does not have to be the same style, but we would like to maintain some brand relevance. There are some other attachments to give you an idea about the look of the company. Also attached is a picture of the dark rum in the bottle. This is what the label will go onto.

-The label will most likely be printed on craft paper stock.

Industry/Entity Type

It Company

Requirements
Must have
• We need the following in the new label
-Company Name= Tallowbrook Distillery
-Product name= Lady Winnow's Cask
-Product sub-name= Aged Heronfield Rum
-Product description= Distilled Bottled and Aged by Tallowbrook Distillery
Nice to have
• We would like to incorporate a rendering of Lady Winnow or just a crown. We think this is important because Charlotte, NC is named after her.

```html
<!DOCTYPE html>
<html lang="en">
<head>
<meta charset="utf-8">
<title>Lady Winnow's Cask – Aged Heronfield Rum Label</title>
<link rel="stylesheet" href="https://fonts.googleapis.com/css2?family=Pinyon+Script&family=Arimo:wght@700&family=Cormorant+Garamond:ital,wght@1,600&family=Libre+Baskerville&display=swap">
<style>
  :root {
    --ink: #16191b;
    --ink-soft: #22272a;
    --gold-light: #f1d99a;
    --gold: #c99a45;
    --gold-deep: #7a5322;
    --band: #d9bf86;
    --cream: #ffffff;
    --rule: #9a8f7a;
    --portrait-hair: #9b7a55;
    --portrait-robe: #7e1f1c;
  }
  * { margin: 0; padding: 0; box-sizing: border-box; }
  html, body { width: 756px; height: 1200px; overflow: hidden; background: var(--cream); }
  .label { position: relative; width: 756px; height: 1200px; }
  .label__art { position: absolute; inset: 0; }
  .title {
    position: absolute; left: 0; right: 0; top: 680px;
    text-align: center;
    font-family: "Pinyon Script", cursive;
    font-size: 84px; line-height: 96px;
    color: var(--gold);
    background: linear-gradient(180deg, var(--gold-light) 15%, var(--gold) 55%, var(--gold-deep) 100%);
    -webkit-background-clip: text; background-clip: text;
    -webkit-text-fill-color: transparent;
  }
  .rule { position: absolute; left: 100px; right: 100px; height: 2px; background: var(--rule); }
  .rule--top { top: 880px; }
  .rule--bottom { top: 952px; }
  .subtitle {
    position: absolute; left: 0; right: 0; top: 890px;
    text-align: center;
    font-family: "Arimo", Arial, sans-serif; font-weight: 700;
    font-size: 44px; color: var(--cream);
  }
  .distillery {
    position: absolute; left: 0; right: 0; top: 1000px;
    text-align: center;
    font-family: "Cormorant Garamond", serif; font-style: italic; font-weight: 600;
    font-size: 46px; color: var(--gold);
  }
  .statement {
    position: absolute; left: 25px; right: 25px; top: 1082px; height: 40px;
    display: flex; align-items: center; justify-content: center;
    font-family: "Libre Baskerville", serif;
    font-size: 21px; color: var(--ink);
  }
</style>
</head>
<body>
<main class="label">
  <svg class="label__art" width="756" height="1200" viewBox="0 0 756 1200" aria-hidden="false">
    <defs>
      <linearGradient id="goldV" x1="0" y1="0" x2="1" y2="0">
        <stop offset="0" stop-color="#7a5322"/>
        <stop offset="0.45" stop-color="#f1d99a"/>
        <stop offset="1" stop-color="#8a6128"/>
      </linearGradient>
      <linearGradient id="goldH" x1="0" y1="0" x2="0" y2="1">
        <stop offset="0" stop-color="#7a5322"/>
        <stop offset="0.45" stop-color="#f1d99a"/>
        <stop offset="1" stop-color="#8a6128"/>
      </linearGradient>
      <linearGradient id="goldRing" x1="0" y1="0" x2="1" y2="1">
        <stop offset="0" stop-color="#f1d99a"/>
        <stop offset="0.5" stop-color="#a8762f"/>
        <stop offset="1" stop-color="#f1d99a"/>
      </linearGradient>
      <linearGradient id="portrait" x1="0" y1="0" x2="0" y2="1">
        <stop offset="0" stop-color="#3a3a3a"/>
        <stop offset="0.35" stop-color="#9b7a55"/>
        <stop offset="0.75" stop-color="#7e1f1c"/>
        <stop offset="1" stop-color="#5a3a1e"/>
      </linearGradient>
      <linearGradient id="band" x1="0" y1="0" x2="0" y2="1">
        <stop offset="0" stop-color="#f0dcaa"/>
        <stop offset="1" stop-color="#c9a45e"/>
      </linearGradient>
    </defs>

    <!-- dark panel -->
    <rect class="panel" x="25" y="25" width="706" height="1150" fill="var(--ink)"/>

    <!-- frame bars -->
    <rect x="32" y="40" width="40" height="1120" fill="url(#goldV)"/>
    <rect x="684" y="40" width="40" height="1120" fill="url(#goldV)"/>
    <rect x="40" y="32" width="676" height="40" fill="url(#goldH)"/>
    <rect x="40" y="1128" width="676" height="40" fill="url(#goldH)"/>

    <!-- corner blocks -->
    <g class="corners" stroke="var(--ink)" stroke-width="6">
      <g><rect x="18" y="18" width="68" height="68" fill="url(#goldH)"/><path d="M18 18L86 86M86 18L18 86"/></g>
      <g><rect x="670" y="18" width="68" height="68" fill="url(#goldH)"/><path d="M670 18L738 86M738 18L670 86"/></g>
      <g><rect x="18" y="1114" width="68" height="68" fill="url(#goldH)"/><path d="M18 1114L86 1182M86 1114L18 1182"/></g>
      <g><rect x="670" y="1114" width="68" height="68" fill="url(#goldH)"/><path d="M670 1114L738 1182M738 1114L670 1182"/></g>
    </g>

    <!-- oval portrait frame -->
    <ellipse cx="378" cy="380" rx="208" ry="272" fill="url(#goldRing)"/>
    <ellipse cx="378" cy="380" rx="190" ry="254" fill="var(--ink-soft)"/>
    <g role="img" aria-label="Portrait of Lady Winnow in an ermine-trimmed red robe">
      <ellipse cx="378" cy="380" rx="188" ry="252" fill="url(#portrait)"/>
    </g>

    <!-- statement band -->
    <rect x="25" y="1080" width="706" height="44" fill="url(#band)" stroke="var(--gold-deep)" stroke-width="2"/>
  </svg>

  <h1 class="title">Lady Winnow's<br>Cask</h1>
  <div class="rule rule--top"></div>
  <p class="subtitle">Aged Heronfield Rum</p>
  <div class="rule rule--bottom"></div>
  <p class="distillery">Tallowbrook Distillery</p>
  <p class="statement">Distilled Bottled and Aged by Tallowbrook Distillery</p>
</main>
</body>
</html>
```